New Poster Design Project

Make an out standing A2 poster with below information,it is out first edition!Use the Attached image as background,Thanx!

Tolvik Meridian Arts Gathering
16 - 22 June 2014
Www.tmagfest.example

Creating a new vision of Africa through African Arts and Culture

Guest speakers / Artists

Delphine Korrato-Væstrup (S.A)
Tekle Berhanu Woldesan (Ethio)
Ronny Bastien-Kolo (Uganda)
Håkon Lunde (Nor)
Velvet Drum Collective (Zim)
Kalumbero Band (Moz,Nor,Swe & Zim)
Dj Zoto Zoto with Afro beats (Ghana/UK )
Dj Marquee/Storm Duchess with collage mix (Bergen)

@ Cafe Lutembe, Nordvik Global Heritage House (Nghh) Helsebrygga,Kjøpmannsplassen,Lindehagen & Vevergangen gate

Mon-Thur
Free entry,food & drinks served

Fri - Entry by donation & Sat - Tmagfest closing ceremony (100kr)
Updates

Project Deadline Extended

Project Deadline Extended
Reason: I made a mistake on extending time on this project now I can not reverse the extended time aaarrrr!!!I really dont have time,The poster should be all over the place by now since Im left with a couple of days away to the festival!!!I need someone to QuickFix me a A2 top notch poster in No time...my deadline is NOW NOW,LATEST Wednesday 21 May 2014,Thanx!

Industry/Entity Type

Cafe

Requirements
Must have
• sponsors logo
Nice to have
• Symbols
Should not have

```html
<!DOCTYPE html>
<html lang="en">
<head>
<meta charset="utf-8">
<title>Tolvik Meridian Arts Gathering – Poster</title>
<link rel="stylesheet" href="https://fonts.googleapis.com/css2?family=Montserrat:wght@300;400;500;600;700&family=Playfair+Display:wght@500&family=Zilla+Slab:wght@400&display=swap">
<style>
  :root{
    --surround:#3d3f3d;
    --ink:#000;
    --orange:#f7941d;
    --teal:#1fd3a6;
    --white:#ffffff;
    --soft:#dcdcdc;
    --muted:#a9a9a9;
    --rule:#8a8a8a;
    --strip:#ffffff;
    --strip-text:#555;
  }
  html,body{margin:0;padding:0;width:1200px;height:1029px;overflow:hidden;background:var(--surround);}
  .stage{position:absolute;left:0;top:0;width:1400px;height:1200px;transform:scale(0.857143);transform-origin:0 0;}
  .poster{position:absolute;left:300px;top:33px;width:800px;height:1133px;background:var(--ink);overflow:hidden;font-family:"Montserrat",sans-serif;}
  .hero-photo{position:absolute;left:200px;top:190px;width:600px;height:837px;
    background:
      radial-gradient(ellipse 46% 38% at 66% 70%, #8a7460 0%, #5a4838 45%, rgba(40,30,24,0) 100%),
      radial-gradient(ellipse 30% 30% at 72% 20%, #d8d2c8 0%, #6b5a4a 50%, rgba(40,30,24,0) 100%),
      linear-gradient(90deg, #000 0%, #120d0a 30%, #2a211b 65%, #3a2e25 100%);}
  .masthead{position:absolute;left:0;top:0;width:800px;height:190px;background:var(--ink);}
  .title-main{position:absolute;left:28px;top:22px;font-family:"Playfair Display",serif;font-weight:500;font-size:124px;line-height:1;color:var(--orange);letter-spacing:-2px;}
  .title-sub{position:absolute;left:478px;top:74px;font-weight:600;font-size:33px;line-height:37px;color:var(--teal);}
  .site{position:absolute;left:44px;top:156px;font-weight:700;font-size:17px;color:var(--white);}
  .dates{position:absolute;left:328px;top:159px;font-weight:700;font-size:17px;color:var(--white);}
  .tagline{position:absolute;left:57px;top:198px;width:400px;margin:0;text-align:center;font-weight:400;font-size:22px;line-height:28px;color:var(--soft);}
  .lineup-heading{position:absolute;left:38px;top:294px;font-family:"Zilla Slab",serif;font-size:24px;color:var(--teal);margin:0;font-weight:400;}
  .lineup{position:absolute;left:31px;top:336px;margin:0;padding:0;list-style:none;font-size:15px;line-height:24px;color:var(--soft);}
  .rule{position:absolute;left:31px;height:1px;}
  .rule--grey{top:544px;width:417px;background:var(--rule);}
  .rule--teal{top:685px;width:294px;background:var(--teal);}
  .venue{position:absolute;left:31px;top:559px;font-style:normal;font-size:18px;line-height:28px;color:var(--white);}
  .venue small{font-size:15px;letter-spacing:.5px;}
  .schedule{position:absolute;left:31px;top:709px;font-weight:700;font-size:20px;line-height:30px;}
  .schedule .day{color:var(--orange);}
  .schedule .note{color:var(--muted);}
  .schedule .gap{height:20px;}
  .sponsors{position:absolute;left:0;top:1027px;width:800px;height:106px;background:var(--strip);}
  .sponsors-label{position:absolute;left:0;top:3px;width:800px;text-align:center;font-size:12px;color:#888;letter-spacing:.5px;}
  .sponsor-row{position:absolute;left:10px;right:10px;top:30px;display:flex;justify-content:space-between;align-items:flex-start;}
  .sponsor{width:106px;display:flex;flex-direction:column;align-items:center;gap:6px;text-align:center;font-weight:600;font-size:11px;line-height:13px;color:var(--strip-text);}
  .sponsor .dot{width:32px;height:32px;border-radius:50%;}
  .sponsor .sq{width:30px;height:30px;margin:1px 0;}
  .sponsor .blank{width:32px;height:32px;}
</style>
</head>
<body>
<div class="stage">
  <main class="poster">
    <div class="hero-photo" role="img" aria-label="Sepia portrait photograph of a smiling performer in a white head wrap, seated and leaning on a round thumb piano"></div>

    <header class="masthead">
      <div class="title-main">Tolvik</div>
      <div class="title-sub">Meridian Arts<br>Gathering</div>
      <div class="site">www.tmagfest.example</div>
      <div class="dates">16 - 22 June 2014</div>
    </header>

    <p class="tagline">Creating a new vision of Africa through African Arts and Culture</p>

    <h2 class="lineup-heading">GUEST SPEAKERS / ARTISTS</h2>
    <ul class="lineup">
      <li>Delphine Korrato-Væstrup (S.A)</li>
      <li>Tekle Berhanu Woldesan (Ethio)</li>
      <li>Ronny Bastien-Kolo (Uganda)</li>
      <li>Håkon Lunde (Nor)</li>
      <li>Velvet Drum Collective (Zim)</li>
      <li>Kalumbero Band (Moz,Nor,Swe &amp; Zim)</li>
      <li>Dj Zoto Zoto with Afro beats (Ghana/UK )</li>
      <li>Dj Marquee/Storm Duchess with collage mix (Bergen)</li>
    </ul>

    <div class="rule rule--grey"></div>

    <address class="venue">
      @ Cafe Lutembe, Nordvik Global Heritage<br>
      House (Nghh) Helsebrygga,<br>
      Kjøpmannsplassen,<br>
      <small>Lindehagen &amp; Vevergangen gate</small>
    </address>

    <div class="rule rule--teal"></div>

    <div class="schedule">
      <div class="day">MON-THUR</div>
      <div class="note">Free entry,</div>
      <div class="note">food &amp; drinks served</div>
      <div class="gap"></div>
      <div class="day">FRI - Entry by donation</div>
      <div class="day">SAT - Tmagfest closing ceremony (100kr)</div>
    </div>

    <footer class="sponsors">
      <div class="sponsors-label">Supported by</div>
      <div class="sponsor-row">
        <div class="sponsor"><span class="sq" style="background:#222"></span>TMAG</div>
        <div class="sponsor"><span class="dot" style="background:var(--orange)"></span>lyskilde.example</div>
        <div class="sponsor"><span class="dot" style="background:#f9a51a"></span>ungfond.example</div>
        <div class="sponsor"><span class="dot" style="background:#c9302c"></span>Tolvik Kommune</div>
        <div class="sponsor"><span class="dot" style="background:#d9141e"></span>Nghh</div>
        <div class="sponsor"><span class="blank"></span>Karibu Dance Ensemble</div>
        <div class="sponsor"><span class="dot" style="background:#7cc242"></span>Dugnadshuset</div>
      </div>
    </footer>
  </main>
</div>
</body>
</html>
```